Orva Business Card

we need a business card for flooring business called Orva Flooring, the design should be black and white. we have 2 locations

Nunawading Showroom
527 Kellerman Road,
Nunawading VIC 3131

Bentleigh Showroom
462 Bramwell Hwy,
Bentleigh VIC 3204

email : sales@orvaflooring.com.au
(03) 9471 2830

Please inform we sell , Laminate, Hybrid, Timber, carpet and commercial flooring

```html
<!DOCTYPE html>
<html lang="en">
<head>
<meta charset="utf-8">
<title>Orva Flooring Business Card</title>
<link href="https://fonts.googleapis.com/css2?family=Crimson+Pro:wght@400;700&display=swap" rel="stylesheet">
<style>
  :root {
    --stage: #2b2b2b;
    --card-dark: #1d1b1b;
    --card-light: #f7f7f7;
    --ink: #111111;
    --ink-soft: #333333;
    --paper: #ffffff;
    --rule: #c9c9c9;
  }
  * { box-sizing: border-box; margin: 0; padding: 0; }
  html, body {
    width: 1200px; height: 900px; overflow: hidden;
    background: var(--stage);
    font-family: "Crimson Pro", Georgia, serif;
  }
  .stage {
    width: 1200px; height: 900px;
    display: flex; flex-direction: column; align-items: center; justify-content: center;
    gap: 36px;
  }
  .card {
    position: relative;
    width: 600px; height: 343px;
    border-radius: 30px;
    overflow: hidden;
  }
  .card--front {
    background: var(--card-dark);
    display: flex; align-items: center; justify-content: center;
  }
  .brand-name {
    font-family: "Crimson Pro", Georgia, serif;
    font-weight: 400;
    letter-spacing: 0.06em;
    text-align: center;
    line-height: 1.05;
  }
  .card--front .brand-name { color: var(--paper); font-size: 52px; }
  .card--back { background: var(--card-light); color: var(--ink); }
  .card--back .brand-name {
    position: absolute; left: 30px; top: 105px; width: 250px;
    color: var(--ink); font-size: 46px;
  }
  .divider { position: absolute; inset: 0; }
  .contact {
    position: absolute; left: 320px; top: 36px;
    list-style: none; font-size: 17px; line-height: 1.2; color: var(--ink-soft);
  }
  .contact li { display: flex; gap: 8px; margin-bottom: 4px; }
  .contact svg { width: 14px; height: 14px; flex: none; margin-top: 3px; fill: var(--ink); }
  .contact .location { margin-top: 4px; }
  .contact strong { color: var(--ink); font-weight: 700; }
  .services {
    position: absolute; left: 0; right: 0; bottom: 30px;
    text-align: center; font-size: 17px; color: var(--ink-soft);
  }
  .services h2 { font-size: 18px; font-weight: 700; color: var(--ink); margin-bottom: 2px; }
</style>
</head>
<body>
<main class="stage">
  <section class="card card--front" aria-label="Card front">
    <p class="brand-name">Orva<br>Flooring</p>
  </section>

  <section class="card card--back" aria-label="Card back">
    <svg class="divider" viewBox="0 0 600 343" aria-hidden="true">
      <line x1="280" y1="20" x2="330" y2="220" stroke="var(--rule)" stroke-width="1"/>
    </svg>
    <p class="brand-name">Orva<br>Flooring</p>

    <ul class="contact">
      <li>
        <svg viewBox="0 0 24 24"><path d="M6.6 10.8a15 15 0 0 0 6.6 6.6l2.2-2.2c.3-.3.7-.4 1-.2 1.1.4 2.3.6 3.6.6.6 0 1 .4 1 1V20c0 .6-.4 1-1 1A17 17 0 0 1 3 4c0-.6.4-1 1-1h3.5c.6 0 1 .4 1 1 0 1.3.2 2.5.6 3.6.1.3 0 .7-.2 1z"/></svg>
        <span>(03) 9471 2830</span>
      </li>
      <li>
        <svg viewBox="0 0 24 24"><path d="M2 5h20v14H2z M2 5l10 8 10-8" fill="none" stroke="currentColor" stroke-width="2"/><path d="M2 5h20l-10 8z"/></svg>
        <span>sales@orvaflooring.com.au</span>
      </li>
      <li class="location">
        <svg viewBox="0 0 24 24"><path d="M12 2a7 7 0 0 0-7 7c0 5 7 13 7 13s7-8 7-13a7 7 0 0 0-7-7zm0 9.5A2.5 2.5 0 1 1 12 6.5a2.5 2.5 0 0 1 0 5z"/></svg>
        <span><strong>Nunawading Showroom</strong><br>527 Kellerman Road,<br>Nunawading VIC 3131</span>
      </li>
      <li class="location">
        <svg viewBox="0 0 24 24"><path d="M12 2a7 7 0 0 0-7 7c0 5 7 13 7 13s7-8 7-13a7 7 0 0 0-7-7zm0 9.5A2.5 2.5 0 1 1 12 6.5a2.5 2.5 0 0 1 0 5z"/></svg>
        <span><strong>Bentleigh Showroom</strong><br>462 Bramwell Hwy,<br>Bentleigh VIC 3204</span>
      </li>
    </ul>

    <div class="services">
      <h2>Our Services</h2>
      <p>Laminate, Hybrid, Timber, Carpet And Commercial Flooring</p>
    </div>
  </section>
</main>
</body>
</html>
```